High Profile Wordpress Design for Marketing Agency

http://www.VantaCom.co.nz is moving from DotNetNuke to wordpress

Vanta PR is a leading New Zealand consumer brands public relations and advertising agency.
Our marketing agency represents some of the worlds most recognisable brands as well as some small independent businesses and everything in between.
Our DNN current site has served us well for 6+ years but we are now wanting to move to wordpress.

We are looking for a new look for our website which will be either a 2013 facelift keeping existing colour scheme rather than a radical new design
Our target market is marketing managers and brand owners familiar with design and marketing elements.
First and foremost the site must be functional from an SEO and loading speed point of view. To assist this we want to retain the text content.
Secondly we have historically had only pointers to other pages on our site but we want to incorporate more of the highlights of our services and our portfolio with the addition of some 'sample boxes' such as in this template: http://layoutbazaar.example/item/sleek-firm-cms-theme/full_screen_preview/7305816

Wordpress offers an easier interface for uploading news items which we do daily and also take advantage of the plugins for seo. We are looking to redesign the look of the site while keeping all the existing text content.

Logo – also needs refreshing. Something corporate but not staid. Modern and clean.

Existing pages
- We want a fresh new clean look while retaining the orange and gray colours. white space is good. modern fonts are good.
- Social media : we want to focus on Google Plus primarily but also facebook and twitter. We suggest a funky design with the social media logos. Social media logos on all pages.
- Add New page: client coverage. A page to showcase new client coverage. Could be print, links to online video, mepgs, etc. Perhaps as a blog?
- Add New page: Advertising (as a service).

Home page. Perhaps a larger image existing image can be used or something new that says Stand out from the crowd (but not in a clichéd way). perhaps 3-4 main images could be used which rotate? We want to use stunning image(s) on the site.
Retain existing body of text somewhere on page.

an alternative idea might be to look at images which relate to news. and use the phrase "journalists reaching journalists"

Add Small ‘boxes’ on home page – teasers for content inside the site:
- Our clients logo box. Perhaps use a mouse over to ‘roll’ logos from homepage? Plus link to our clients page. http://www.vantacom.co.nz/OurClients/CurrentClients.aspx
- Our services
- Quotes about us. Show an image of Horizonte magazine with quote about us
- Advertising box: Featured project (as embedded youtube clip and link case study)
- Contact us page – refresh look simple details only.

Client News (blog) page:

Image(s) to top right rather than bottom.
Google Plus like one and share as first icon. Also facebook, twitter share and RSS. (moving icons which scroll down as reader moves down?)

Budget Increase to A$2190
Hi Budget on this project to redesign Auckland PR Firm Vanta PR's website in wordpress has been increased significantly to A$2190

Target Market(s)

Marketing managers, small - large business owners
we are primarily a public relations firm, then advertising. focus should be on these services rather than web design/seo etc which are a secondary part of our offering.

Industry/Entity Type

Advertising

Requirements
Must have
• must retain existing text content(for seo reasons)
fast loading, free of slow graphics
mobile/tablet friendly
new logo
Google Plus 1 logo
Should not have
• our agency is slightly on the conservative side and yet we are looking for a modern look.
prefer light over dark colour scheme/images
Images – better to not use people in images. people from stock images tend to give the impression of an international site and we are looking closer to NZ

```html
<!DOCTYPE html>
<html lang="en">
<head>
<meta charset="utf-8">
<title>Vanta PR</title>
<link rel="stylesheet" href="https://fonts.googleapis.com/css2?family=Open+Sans:ital,wght@0,300;0,400;0,600;0,700;1,300&display=swap">
<style>
:root{
  --orange:#f26a10;
  --orange-deep:#e8520a;
  --orange-light:#f7931e;
  --ink:#3a3a3a;
  --grey:#6b6b6b;
  --grey-light:#9a9a9a;
  --line:#dcdcdc;
  --panel:#f7f7f7;
  --dark:#2b2b2b;
  --white:#ffffff;
}
*{box-sizing:border-box;margin:0;padding:0}
html,body{width:1047px;height:1200px;overflow:hidden;background:var(--white)}
body{font-family:"Open Sans",Arial,sans-serif;color:var(--ink)}
.page{position:relative;width:1047px;height:1200px;overflow:hidden;background:#fff}
.abs{position:absolute}
.top-rule{left:0;top:0;width:1047px;height:3px;background:linear-gradient(90deg,#f7a35c,var(--orange),#f7a35c)}

/* header */
.brand{left:255px;top:18px;font-size:22px;font-weight:300;letter-spacing:.5px;color:#555}
.brand span{color:#a0a0a0}
.search{left:578px;top:20px;width:142px;height:22px;background:#eeeeee;border:1px solid #dedede;border-radius:2px;font-size:7.5px;color:#999;padding:6px 0 0 10px}
.search svg{position:absolute;right:7px;top:5px}
.login{left:731px;top:20px;width:59px;height:22px;background:var(--orange);border-radius:2px;color:#fff;font-size:7.5px;font-weight:600;padding:6px 0 0 24px}
.login svg{position:absolute;left:12px;top:6px}

/* hero */
.hero{left:197px;top:59px;width:653px;height:180px;background:radial-gradient(ellipse at 72% 55%,#8a8a8a 0%,#4a4a4a 35%,#1e1e1e 70%,#0e0e0e 100%)}
.hero-title{left:255px;top:122px;font-size:26px;font-weight:300;line-height:26px;color:var(--orange)}
.hero-title span{display:block;color:#fff;font-size:19px;line-height:22px}
.hero-rule{left:255px;top:176px;width:186px;height:1px;background:#555}
.hero-dots{left:256px;top:186px;display:flex;gap:5px}
.hero-dots i{display:block;width:3px;height:3px;border-radius:50%;background:#777}
.hero-dots i.on{width:5px;height:5px;margin-top:-1px;border:1px solid var(--orange);background:transparent}
.arrow{top:131px;width:33px;height:34px}
.arrow-left{left:163px}
.arrow-right{left:850px}

.nav{left:197px;top:239px;width:653px;height:40px;background:linear-gradient(#4a4a4a,#333 50%,#2a2a2a);box-shadow:0 12px 18px -10px rgba(0,0,0,.45)}
.nav-item{position:absolute;top:15px;font-size:7.5px;color:#ddd;letter-spacing:.2px}
.nav-item.active{color:#fff}
.nav-item .caret{font-size:5px;margin-left:3px;vertical-align:1px}
.nav-active-bar{left:256px;top:276px;width:23px;height:2px;background:var(--orange)}

.dropdown{left:522px;top:271px;width:213px;height:104px;background:linear-gradient(var(--orange),var(--orange-deep));box-shadow:0 3px 8px rgba(0,0,0,.25);z-index:5}
.dropdown-tab{left:522px;top:245px;width:87px;height:27px;background:var(--orange);z-index:5;color:#fff;font-size:7.5px;font-weight:600;padding:9px 0 0 14px}
.dropdown-col{position:absolute;top:15px;list-style:none;font-size:6.5px;color:#fff;white-space:nowrap}
.dropdown-col li{height:16.3px}
.dropdown-col li.current{font-weight:700}
.dropdown-col li.current::before{content:"\25B8";font-size:5px;margin:0 4px 0 -6px}
.dropdown-divider{position:absolute;left:116px;top:14px;width:1px;height:70px;background:rgba(255,255,255,.25)}

/* quote band */
.quote-band{left:0;top:314px;width:1047px;height:66px;background:#ededed}
.quote-marks{font-size:78px;font-weight:700;color:#dcdcdc;line-height:1}
.quote-text{left:263px;top:331px;font-size:12.5px;font-style:italic;font-weight:300;color:#555;letter-spacing:.2px;white-space:nowrap}
.quote-source{left:483px;top:353px;font-size:7.5px;color:#999;letter-spacing:.5px}

/* who we are */
.about-title{left:268px;top:406px;font-size:15px;font-weight:300;color:#333}
.about-rule{left:255px;top:433px;width:307px;height:2px;background:var(--line)}
.about-body{left:268px;top:448px;width:296px;font-size:6.6px;line-height:11.4px;color:#444}
.about-body p{margin-bottom:11.4px}
.btn-orange{background:var(--orange);color:#fff;font-size:7px;font-weight:600;border-radius:2px;text-align:center}
.read-more{left:268px;top:666px;width:118px;height:22px;padding-top:6px}

/* services */
.services{left:583px;top:397px;width:207px;height:296px;background:var(--panel);border:1px solid #e4e4e4}
.services-head{position:absolute;left:0;top:0;width:100%;height:37px;background:#fff;border-bottom:1px solid #eee}
.services-title{position:absolute;left:0;top:10px;width:100%;text-align:center;font-size:15px;font-weight:300;color:#333}
.services-tab{position:absolute;left:66px;top:37px;width:74px;height:4px;background:var(--orange)}
.services-list{position:absolute;left:0;top:55px;width:100%;list-style:none;text-align:center;font-size:9px;color:#555;letter-spacing:.2px}
.services-list li{height:22.9px;line-height:22.9px}
.services-list li.highlight{margin:0 11px;background:var(--orange);color:#fff;border-radius:1px}

/* clients */
.clients-band{left:0;top:737px;width:1047px;height:148px;background:radial-gradient(ellipse at 50% 90%,#d8d8d8 0%,#b4b4b4 45%,#999 100%)}
.clients-title{left:0;top:748px;width:1047px;text-align:center;font-size:10px;color:#fff;letter-spacing:.3px}
.clients-box{left:256px;top:770px;width:534px;height:62px;background:#fff;box-shadow:0 2px 4px rgba(0,0,0,.2);display:flex;align-items:center;justify-content:space-around;padding:0 12px}
.client-name{display:flex;align-items:center;gap:5px;font-size:11.5px;font-weight:600;color:#3a3a3a}
.client-name i{display:block;width:7px;height:7px;background:#3a3a3a}
.clients-pager{left:720px;top:764px;width:60px;height:10px;background:linear-gradient(#eee,#aaa);border-radius:2px;display:flex;gap:4px;justify-content:center;align-items:center}
.clients-pager i{display:block;width:3px;height:3px;border-radius:50%;background:#777}
.clients-pager i.on{width:5px;height:5px;background:#333}
.portfolio-btn{left:447px;top:845px;width:153px;height:22px;border:1px solid #ddd;color:#fff;font-size:7.5px;text-align:center;padding-top:6px}

/* contact */
.contact{left:0;top:888px;width:1047px;height:236px;background:radial-gradient(ellipse at 70% 100%,var(--orange-light) 0%,#f27b10 35%,var(--orange-deep) 75%)}
.contact-tab{left:438px;top:888px}
.contact-title{left:438px;top:891px;width:171px;text-align:center;font-size:15px;font-weight:300;color:#777}
.field{background:var(--orange-deep);border:1px solid rgba(255,255,255,.12);color:#fff;font-size:7.5px;padding:8px 0 0 10px;box-shadow:inset 0 1px 2px rgba(0,0,0,.15)}
.field-name{left:337px;top:945px;width:176px;height:28px}
.field-email{left:337px;top:983px;width:176px;height:28px}
.field-phone{left:337px;top:1022px;width:176px;height:28px}
.field-message{left:534px;top:945px;width:176px;height:105px}
.send{left:469px;top:1068px;width:109px;height:27px;background:linear-gradient(#4a4a4a,#2a2a2a);border-radius:2px;color:#fff;font-size:11px;padding:6px 0 0 29px;box-shadow:0 2px 3px rgba(0,0,0,.3)}
.send svg{position:absolute;left:67px;top:8px}

/* footer */
.footer-links{left:259px;top:1136px;font-size:6.3px;color:#aaa;white-space:nowrap}
.footer-links a{color:#aaa;text-decoration:none}
.footer-links a.current{color:var(--orange);text-decoration:underline}
.footer-links .sep{margin:0 3px}
.copyright{left:709px;top:1136px;font-size:6.3px;color:#555}
</style>
</head>
<body>
<div class="page">
  <div class="abs top-rule"></div>

  <header>
    <div class="abs brand">VANTA <span>PR</span></div>
    <div class="abs search">SEARCH TERM HERE...
      <svg width="10" height="10" viewBox="0 0 10 10"><circle cx="4" cy="4" r="3" fill="none" stroke="#f26a10" stroke-width="1.3"/><line x1="6.3" y1="6.3" x2="9" y2="9" stroke="#f26a10" stroke-width="1.5"/></svg>
    </div>
    <div class="abs login">
      <svg width="7" height="9" viewBox="0 0 7 9"><path d="M1.5 4V2.6a2 2 0 0 1 4 0V4" fill="none" stroke="#fff" stroke-width="1"/><rect x="0.5" y="4" width="6" height="4.5" fill="#fff"/></svg>
      LOGIN
    </div>
  </header>

  <section>
    <div class="abs hero" role="img" aria-label="Aerial photograph of a dark crowd with one figure standing in a spotlight"></div>
    <h1 class="abs hero-title">STAND OUT<span>FROM THE CROWD.</span></h1>
    <div class="abs hero-rule"></div>
    <div class="abs hero-dots"><i class="on"></i><i></i><i></i><i></i></div>

    <svg class="abs arrow arrow-left" viewBox="0 0 33 34"><path d="M8 0H33V34H8L0 17Z" fill="#d6d6d6"/><path d="M20 12l-5 5 5 5" fill="none" stroke="#fff" stroke-width="2"/></svg>
    <svg class="abs arrow arrow-right" viewBox="0 0 33 34"><path d="M0 0H25L33 17L25 34H0Z" fill="#d6d6d6"/><path d="M14 12l5 5-5 5" fill="none" stroke="#fff" stroke-width="2"/></svg>

    <nav class="abs nav">
      <span class="nav-item active" style="left:59px">HOME</span>
      <span class="nav-item" style="left:114px">OUR SERVICES<span class="caret">&#9660;</span></span>
      <span class="nav-item" style="left:202px">NEWS<span class="caret">&#9660;</span></span>
      <span class="nav-item" style="left:262px">OUR PEOPLE</span>
      <span class="nav-item" style="left:427px">OUR CLIENTS<span class="caret">&#9660;</span></span>
      <span class="nav-item" style="left:512px">CONTACT US</span>
    </nav>
    <div class="abs nav-active-bar"></div>

    <div class="abs dropdown-tab">CASE STUDIES <span style="font-size:5px;margin-left:3px">&#9660;</span></div>
    <div class="abs dropdown">
      <ul class="dropdown-col" style="left:14px">
        <li>SkinCheck Australasia</li>
        <li class="current">Pivot Tablet</li>
        <li>Mowcraft</li>
        <li>Vodka Brand Launch</li>
        <li>roamcoach.com</li>
      </ul>
      <div class="dropdown-divider"></div>
      <ul class="dropdown-col" style="left:128px">
        <li>Lakeside Hotel Rotorua</li>
        <li>Harbourline Style Week</li>
        <li>The Inked Heart</li>
        <li>Evan Wilder</li>
      </ul>
    </div>
  </section>

  <section>
    <div class="abs quote-band"></div>
    <div class="abs quote-marks" style="left:255px;top:298px">&#8220;</div>
    <div class="abs quote-marks" style="left:752px;top:330px">&#8221;</div>
    <p class="abs quote-text">&#8220;THE KIND OF EXTERNAL PR EXPERTISE THAT SMALL BUSINESSES ARE SCREAMING OUT FOR ..&#8221;</p>
    <p class="abs quote-source">HORIZONTE MAGAZINE</p>
  </section>

  <section>
    <h2 class="abs about-title">WHO WE ARE?</h2>
    <div class="abs about-rule"></div>
    <div class="abs about-body">
      <p>Our experienced public relations specialists bring together a wealth of experience in public relations (PR), market research, magazines, FMCG / food and beverage marketing, television, and editorial journalism. We help our clients get closer to the mind of their target customer than they have ever been before.</p>
      <p>At Vanta PR, our marketing &amp; communications experts will work closely with you as your New Zealand public relations firm and if required, even as your advertising agency. Unlike many other public relations companies we also plan and buy media &#8211; however one of our key points of difference is our ability to enhance your brand equity by integrating your TV, print or digital marketing spend with an effective public relations strategy.</p>
      <p>Whether you are a small independent retailer or a large multinational corporation our Auckland PR agency has a solid branding solution for your budget.</p>
      <p>But don't just take our word for it; respected New Zealand business publication Horizonte magazine recently commented that Vanta PR's award winning director Maren Hollis provides &#8220;...the kind of external Public Relations expertise that small businesses are screaming out for...&#8221;.</p>
    </div>
    <div class="abs btn-orange read-more">READ MORE ABOUT US &nbsp;&#8250;</div>

    <aside class="abs services">
      <div class="services-head"><h2 class="services-title">OUR SERVICES</h2></div>
      <div class="services-tab"></div>
      <ul class="services-list">
        <li>PUBLIC RELATIONS</li>
        <li>ADVERTISING</li>
        <li>MEDIA TRAINING</li>
        <li>SOCIAL MEDIA</li>
        <li class="highlight">ONLINE REPUTATION MANAGEMENT</li>
        <li>CELEBRITY APPERANCES</li>
        <li>COPYWRITING</li>
        <li>EVENTS</li>
        <li>SEO</li>
        <li>WEB DESIGN</li>
      </ul>
    </aside>
  </section>

  <section>
    <div class="abs clients-band"></div>
    <h2 class="abs clients-title" style="font-weight:400">OUR CLIENTS</h2>
    <div class="abs clients-box">
      <span class="client-name"><i></i>Brightline</span>
      <span class="client-name"><i></i>Dentaro</span>
      <span class="client-name"><i></i>Lumifilm</span>
      <span class="client-name"><i></i>Corvelle</span>
      <span class="client-name"><i></i>Sheen'n Simple</span>
    </div>
    <div class="abs clients-pager"><i></i><i class="on"></i><i></i><i></i><i></i></div>
    <div class="abs portfolio-btn">SEE OUR WHOLE PORTFOLIO &nbsp;&#8250;</div>
  </section>

  <section>
    <div class="abs contact"></div>
    <svg class="abs contact-tab" width="171" height="31" viewBox="0 0 171 31"><path d="M0 0H171L154 31H17Z" fill="#fff"/></svg>
    <h2 class="abs contact-title">CONTACT US</h2>
    <div class="abs field field-name">YOUR NAME</div>
    <div class="abs field field-email">YOUR EMAIL</div>
    <div class="abs field field-phone">YOUR PHONE</div>
    <div class="abs field field-message">MESSAGE HERE</div>
    <div class="abs send">SEND!
      <svg width="13" height="10" viewBox="0 0 13 10"><path d="M1 5l4 4 7-8" fill="none" stroke="#fff" stroke-width="2"/></svg>
    </div>
  </section>

  <footer>
    <div class="abs footer-links">
      <a>Home</a><span class="sep">|</span><a>News</a><span class="sep">|</span><a>Our Services</a><span class="sep">|</span><a class="current">Our People</a><span class="sep">|</span><a>Case Studies</a><span class="sep">|</span><a>Our Clients</a><span class="sep">|</span><a>Contact us</a><span class="sep">|</span><a>Terms Of Use</a><span class="sep">|</span><a>Privacy Statement</a><span class="sep">|</span><a>Login</a>
    </div>
    <div class="abs copyright">&#169; 2013 Vanta PR Limited</div>
  </footer>
</div>
</body>
</html>
```